Post Card Design - Photo on front, details on back. Logo on both sides.

Back: See the photo of my old card. The back worked well, as it gave me lots of space to write on. The address details are still correct, but the logo has changed to Josephine Sans. Logo can be on one line or on two (if two, align it on the left).
Don't include the 'BEAUTIFUL WEDDING DRESSES...' bit.
I'd like to print this on thicker, slightly coarse paper, so don't go too small on detail.
Here are the Plume paper details: Paper Stock: Natural Uncoated
Paper Thickness: Premium
Finish: None
Front of Card: I'd like to see options for both pictures:
I think the painted image would look best with a frame in a pale shade and the logo in the frame fairly subtle.
The actual dress photo I'd like to see cropped a bit like in my mock up. You'll need to have a look at how the logo would be best placed on this. You can place it anywhere, or add a banner.
See my website for my brand's look: mirabeltoft.co.nz
Target Market(s)
Brides
Industry/Entity Type
Wedding Dresses
Contact Information for Business Card
Front: Photo and logo. Back: with details and lots of empty space. See attached photos for loose brief.
Other font styles liked:
- Josephine Sans
Requirements
Must have
- I hand-write the gown designs and price on the back of the card, so there needs to be plenty of empty space.
Nice to have
- As per brief.
Should not have
- It must look clean, romantic, modern. Timeless.

```html
<!DOCTYPE html>
<html lang="en">
<head>
<meta charset="utf-8">
<title>Vista Plume – Business Cards</title>
<link rel="stylesheet" href="https://fonts.googleapis.com/css2?family=Josefin+Sans:wght@300;400&display=swap">
<style>
  :root {
    --backdrop: #8a8a8a;
    --gold-light: #efdcae;
    --gold: #dcc08a;
    --gold-deep: #cfae72;
    --ink: #1d1a17;
    --paper: #ffffff;
    --band: #9a9a9a;
    --bloom-pink: #f0a9a6;
    --bloom-cream: #f6ead2;
  }
  * { margin: 0; padding: 0; box-sizing: border-box; }
  html, body { width: 1200px; height: 932px; overflow: hidden; }
  body {
    background: var(--backdrop);
    font-family: "Josefin Sans", sans-serif;
    position: relative;
  }
  .card {
    position: absolute;
    border-radius: 26px;
    overflow: hidden;
    box-shadow: 0 10px 30px rgba(0,0,0,.35);
  }
  /* Front */
  .card-front {
    left: 60px; top: 146px;
    width: 400px; height: 640px;
    background: radial-gradient(ellipse at 50% 40%, var(--gold-light) 0%, var(--gold) 60%, var(--gold-deep) 100%);
  }
  .front-artwork {
    position: absolute;
    left: 40px; top: 60px;
    width: 320px; height: 400px;
    border-radius: 48% 52% 46% 54% / 50% 50% 50% 50%;
    background: radial-gradient(ellipse at 45% 45%, var(--bloom-cream) 0%, #f3cdb9 40%, var(--bloom-pink) 70%, rgba(240,169,166,0) 100%);
  }
  .front-name {
    position: absolute;
    left: 0; right: 0; top: 512px;
    text-align: center;
    font-weight: 300;
    font-size: 34px;
    letter-spacing: 5px;
    color: var(--ink);
    white-space: nowrap;
  }
  .front-url {
    position: absolute;
    left: 0; right: 0; top: 562px;
    text-align: center;
    font-weight: 300;
    font-size: 15px;
    letter-spacing: 5px;
    color: var(--ink);
    white-space: nowrap;
  }
  /* Back */
  .card-back {
    left: 510px; top: 266px;
    width: 640px; height: 400px;
    background: var(--paper);
  }
  .back-rule {
    position: absolute;
    left: 30px; top: 0;
    width: 1px; height: 40px;
    background: var(--ink);
  }
  .back-name {
    position: absolute;
    left: 44px; top: 32px;
    font-weight: 300;
    font-size: 38px;
    line-height: 40px;
    letter-spacing: 6px;
    color: var(--ink);
  }
  .back-contact {
    position: absolute;
    left: 44px; top: 126px;
    list-style: none;
    font-weight: 300;
    font-size: 15px;
    line-height: 24px;
    letter-spacing: 1.5px;
    color: var(--ink);
    white-space: nowrap;
  }
  .back-band {
    position: absolute;
    left: 0; right: 0; bottom: 0;
    height: 24px;
    background: var(--band);
  }
</style>
</head>
<body>
  <section class="card card-front">
    <div class="front-artwork" role="img" aria-label="Vintage painted illustration of a bride and groom embracing amid pink and peach blossoms"></div>
    <p class="front-name">VISTA PLUME</p>
    <p class="front-url">MIRABELTOFT.CO.NZ</p>
  </section>

  <section class="card card-back">
    <span class="back-rule"></span>
    <h1 class="back-name">VISTA<br>PLUME</h1>
    <ul class="back-contact">
      <li>Call : +64 9 555 0148</li>
      <li>Email : vista@mirabeltoft.co.nz</li>
      <li>Web : mirabeltoft.co.nz</li>
    </ul>
    <div class="back-band"></div>
  </section>
</body>
</html>
```